Modern Billboard Ad for Criminal Defense Firm

10.5 x 36 We're looking for something to set us apart from the local competition. Looking for sleek and modern. We're a mid-sized firm in a small market city. We want to give the artist room to be creative on this one.
Thanks

Target Market(s)

Adult clients who have been charged with a crime/DWI

Industry/Entity Type

legal

Font styles to use
Serif
Sans Serif

Requirements
Must have
• Needs to have the firm name in large lettering. Law Offices of Marcus T Whitfield. “PLLC” does not have to be included. Phone number of (555) 384-1927 should be included but not the main focus.
Nice to have
• A call to action or something similar. “Don’t go it alone, call today.”, “ Arrested?”

```html
<!DOCTYPE html>
<html lang="en">
<head>
<meta charset="utf-8">
<title>Law Offices of Marcus T Whitfield – Billboard</title>
<link rel="stylesheet" href="https://fonts.googleapis.com/css2?family=Montserrat:wght@600;700;800;900&family=Playfair+Display:wght@700&display=swap">
<style>
  :root {
    --navy: #0d1b30;
    --navy-deep: #081426;
    --blue: #1570c9;
    --blue-bright: #1a85dc;
    --gold: #b39a6a;
    --white: #ffffff;
    --ink: #111417;
    --page: #eceef1;
  }
  html, body {
    margin: 0;
    width: 1200px;
    height: 900px;
    overflow: hidden;
    background: var(--page);
  }
  .billboard {
    position: absolute;
    left: 40px;
    top: 287px;
    width: 1120px;
    height: 326px;
    overflow: hidden;
    background: var(--navy);
    box-shadow: 0 10px 30px rgba(0,0,0,.18);
  }
  .billboard__shapes {
    position: absolute;
    inset: 0;
    width: 100%;
    height: 100%;
  }
  .billboard__text { position: absolute; margin: 0; }
  .firm-label {
    left: 430px;
    top: 22px;
    width: 640px;
    text-align: center;
    font: 700 24px/1 "Montserrat", sans-serif;
    letter-spacing: 0.42em;
    color: var(--ink);
  }
  .firm-name {
    left: 380px;
    top: 58px;
    width: 730px;
    text-align: center;
    font: 700 68px/1 "Playfair Display", serif;
    color: var(--blue);
    white-space: nowrap;
  }
  .tagline {
    left: 218px;
    top: 196px;
    color: var(--white);
    font-family: "Montserrat", sans-serif;
    font-weight: 800;
    line-height: 1;
    text-transform: uppercase;
  }
  .tagline__lead { display: block; font-size: 16px; letter-spacing: 0.01em; }
  .tagline__action { display: block; font-size: 24px; margin-top: 3px; }
  .headline {
    left: 515px;
    top: 206px;
    font: 800 58px/1 "Montserrat", sans-serif;
    color: var(--white);
    letter-spacing: 0.01em;
  }
  .contact {
    left: 398px;
    top: 288px;
    font: 600 20px/1 "Montserrat", sans-serif;
    color: var(--white);
    letter-spacing: 0.18em;
    white-space: nowrap;
  }
  .contact__number { margin-left: 14px; letter-spacing: 0.1em; }
</style>
</head>
<body>
  <main class="billboard">
    <svg class="billboard__shapes" viewBox="0 0 1120 326" aria-hidden="false">
      <defs>
        <linearGradient id="portraitTone" x1="0" y1="0" x2="1" y2="1">
          <stop offset="0" stop-color="#3a3d42"/>
          <stop offset="0.55" stop-color="#8c8f93"/>
          <stop offset="1" stop-color="#55585c"/>
        </linearGradient>
      </defs>
      <rect class="panel-base" x="0" y="0" width="1120" height="326" fill="var(--navy)"/>
      <polygon class="panel-white" points="335,0 1120,0 1120,188 260,188" fill="var(--white)"/>
      <polygon class="portrait" points="0,0 300,0 205,326 0,326" fill="url(#portraitTone)"
               role="img" aria-label="Black and white portrait of the attorney in a suit, holding a jacket over his shoulder"/>
      <polygon class="stripe stripe--blue" points="318,0 338,0 243,326 223,326" fill="var(--blue-bright)"/>
      <polygon class="stripe stripe--dark" points="300,0 318,0 223,326 205,326" fill="var(--navy-deep)"/>
      <polygon class="panel-gold" points="262,188 505,188 478,268 236,268" fill="var(--gold)"/>
      <polygon class="panel-call" points="495,272 1120,272 1120,326 478,326" fill="var(--blue)"/>
      <rect class="award-badge" x="1036" y="244" width="56" height="74" fill="var(--blue-bright)"/>
    </svg>

    <p class="billboard__text firm-label">LAW OFFICES OF</p>
    <h1 class="billboard__text firm-name">Marcus T Whitfield</h1>
    <p class="billboard__text tagline">
      <span class="tagline__lead">Don’t go it alone,</span>
      <span class="tagline__action">Call today.</span>
    </p>
    <p class="billboard__text headline">ARRESTED?</p>
    <p class="billboard__text contact">CALL US:<span class="contact__number">(555) 384-1927</span></p>
  </main>
</body>
</html>
```